Hi there,

I offer a new set of packages in my cosmetic clinic. It is a down to earth clinic that provides natural results. My clinic has got a natural look.
My website is www.morvela.co.nz
I need one A4 flat leaflet for every package and the special. The leaflets can look of similar design.
Preferred colors are blue/white/silver and green.

```html
<!DOCTYPE html>
<html lang="en">
<head>
<meta charset="utf-8">
<title>Morvela Cosmetic Clinic – Micro-needling Packages</title>
<link rel="stylesheet" href="https://fonts.googleapis.com/css2?family=Fira+Sans:wght@400;500;600;700&family=Montserrat:wght@700;800&display=swap">
<style>
  :root {
    --navy: #083a72;
    --blue: #0d5ea6;
    --sky: #27a8e1;
    --silver: #8a8d91;
    --ink: #1c1c1c;
    --charcoal: #2f2f31;
    --paper: #ffffff;
    --stage: #e6e7e9;
    --panel: #efefef;
  }
  * { box-sizing: border-box; margin: 0; padding: 0; }
  html, body { width: 990px; height: 1200px; overflow: hidden; background: var(--stage); }
  body { font-family: "Fira Sans", sans-serif; color: var(--ink); }

  .flyer {
    position: absolute; left: 70px; top: 0;
    width: 849px; height: 1200px;
    background: var(--paper); overflow: hidden;
  }
  .decor { position: absolute; inset: 0; }

  .brand {
    position: absolute; left: 46px; top: 68px;
    display: flex; align-items: center; gap: 14px;
  }
  .brand-dot { width: 42px; height: 42px; border-radius: 50%; background: var(--sky); }
  .brand-name { font-size: 30px; font-weight: 500; color: var(--silver); letter-spacing: 0.5px; line-height: 1.05; }

  .photo {
    position: absolute; left: 399px; top: 62px;
    width: 486px; height: 486px; border-radius: 50%;
    background: radial-gradient(circle at 45% 55%, #e9c7b4 0%, #cfa18a 40%, #8d7469 75%, #5e514c 100%);
  }

  .tagline {
    position: absolute; left: 114px; top: 238px;
    line-height: 1;
  }
  .tagline .small { display: block; font-size: 33px; font-weight: 600; color: #fff; }
  .tagline .big { display: block; font-size: 66px; font-weight: 700; color: var(--navy); letter-spacing: -1px; }
  .tagline .l1 { margin-bottom: -6px; }
  .tagline .l3 { margin-top: 4px; margin-bottom: -10px; }
  .tagline .l4 { font-size: 80px; }

  .title {
    position: absolute; left: 78px; top: 529px;
    border-left: 3px solid var(--sky); padding-left: 16px;
  }
  .title h1 { font-size: 68px; font-weight: 600; color: var(--navy); line-height: 0.95; letter-spacing: -1px; }
  .title h2 { font-size: 46px; font-weight: 600; color: var(--silver); line-height: 1; margin-top: 2px; }

  .intro {
    position: absolute; left: 76px; top: 654px; width: 648px;
    font-size: 14.6px; font-weight: 500; line-height: 1.32;
  }
  .benefit {
    position: absolute; left: 78px; top: 711px; width: 625px;
    border-left: 2px solid var(--sky); padding-left: 12px;
    font-size: 19.5px; font-weight: 500; color: var(--navy); line-height: 1.25;
  }

  .package {
    position: absolute; top: 781px; height: 64px; display: flex;
    filter: drop-shadow(0 8px 6px rgba(0,0,0,0.18));
  }
  .package .label {
    width: 153px; background: linear-gradient(90deg, #f7f7f7, var(--panel));
    display: flex; align-items: center; padding-left: 24px;
    font-size: 15.5px; font-weight: 500; color: var(--navy); line-height: 1.1;
  }
  .package .price {
    width: 159px; border-radius: 0 4px 4px 0;
    background: linear-gradient(110deg, var(--navy) 0%, var(--blue) 50%, var(--sky) 100%);
    color: #fff; text-align: center; font-family: "Montserrat", sans-serif;
    display: flex; flex-direction: column; justify-content: center;
  }
  .package .amount { font-size: 29px; font-weight: 800; line-height: 1; }
  .package .save { font-size: 15.5px; font-weight: 700; letter-spacing: 0.5px; margin-top: 2px; }
  .package-3 { left: 78px; }
  .package-6 { left: 438px; }

  .facial-banner {
    position: absolute; left: 246px; top: 888px; width: 357px; height: 37px;
    background: linear-gradient(90deg, var(--navy), var(--blue) 70%, var(--sky));
    color: #fff; font-size: 21.5px; font-weight: 500;
    display: flex; align-items: center; justify-content: center;
  }

  .facial {
    position: absolute; top: 947px; width: 160px;
  }
  .facial .desc {
    border-left: 1.5px solid var(--navy); padding-left: 11px;
    font-size: 13.2px; font-weight: 500; line-height: 1.28; height: 36px;
  }
  .facial .tag {
    margin-top: 8px; display: flex; height: 22px;
    font-family: "Montserrat", sans-serif; font-weight: 800; color: #fff; font-size: 14px;
  }
  .facial .tag .amount { width: 64px; background: var(--navy); display: flex; align-items: center; justify-content: center; }
  .facial .tag .save { flex: 1; background: var(--charcoal); display: flex; align-items: center; justify-content: center; letter-spacing: 0.3px; }
  .facial-1 { left: 61px; }
  .facial-2 { left: 250px; }
  .facial-3 { left: 439px; }
  .facial-4 { left: 628px; }

  .terms {
    position: absolute; right: 61px; top: 1104px;
    font-size: 10.8px; font-weight: 500; color: #fff;
  }
  .contacts {
    position: absolute; left: 60px; right: 60px; top: 1140px;
    display: flex; align-items: center; justify-content: space-between;
    color: #fff; font-size: 21px; font-weight: 500;
  }
  .contact { display: flex; align-items: center; gap: 8px; }
  .contact svg { width: 17px; height: 17px; }
  .divider { width: 2px; height: 18px; background: #fff; }
</style>
</head>
<body>
<main class="flyer">
  <svg class="decor" viewBox="0 0 849 1200" width="849" height="1200" aria-hidden="true">
    <defs>
      <linearGradient id="band" x1="0" y1="0" x2="1" y2="0">
        <stop offset="0" stop-color="#0a4a8a"/>
        <stop offset="0.55" stop-color="#1478c0"/>
        <stop offset="1" stop-color="#27a8e1"/>
      </linearGradient>
      <linearGradient id="footer" x1="0" y1="0" x2="1" y2="1">
        <stop offset="0" stop-color="#1a86c9"/>
        <stop offset="1" stop-color="#083f7c"/>
      </linearGradient>
      <linearGradient id="greySweep" x1="0" y1="0" x2="1" y2="0">
        <stop offset="0" stop-color="#2a2a2c"/>
        <stop offset="1" stop-color="#9a9a9c"/>
      </linearGradient>
    </defs>
    <path d="M0,420 C140,368 300,345 470,346 L470,436 C300,432 140,470 0,545 Z" fill="url(#band)"/>
    <path d="M690,500 C760,540 815,580 849,625 L849,605 C815,565 770,520 720,490 Z" fill="#27a8e1"/>
    <path d="M700,510 C770,550 820,590 849,630 L849,622 C818,580 768,540 712,505 Z" fill="#0d5ea6"/>
    <path d="M0,1010 C120,1070 230,1100 345,1112 C220,1110 110,1095 0,1074 Z" fill="url(#greySweep)"/>
    <path d="M0,1074 C160,1110 330,1118 500,1105 C640,1092 760,1050 849,1000 L849,1200 L0,1200 Z" fill="url(#footer)"/>
    <circle cx="196" cy="340" r="147" fill="#27a8e1"/>
    <path d="M275,222 A138,138 0 0 0 70,415" fill="none" stroke="#fff" stroke-width="1.3"/>
    <path d="M100,440 A138,138 0 0 0 300,432" fill="none" stroke="#fff" stroke-width="1.3"/>
    <circle cx="275" cy="222" r="3" fill="#fff"/>
    <circle cx="300" cy="432" r="3" fill="#fff"/>
    <line x1="114" y1="433" x2="180" y2="433" stroke="#fff" stroke-width="2.5"/>
  </svg>

  <div class="brand">
    <span class="brand-dot"></span>
    <span class="brand-name">Morvela Cosmetic Clinic</span>
  </div>

  <div class="photo" role="img" aria-label="Photo of a client receiving a micro-needling skin treatment"></div>
  <svg class="decor" viewBox="0 0 849 1200" width="849" height="1200" aria-hidden="true">
    <circle cx="642" cy="305" r="230" fill="none" stroke="#27a8e1" stroke-width="1.3"/>
    <circle cx="642" cy="535" r="3.5" fill="#27a8e1"/>
  </svg>

  <div class="tagline">
    <span class="small l1">Meticulous</span>
    <span class="big l2">approach</span>
    <span class="small l3">to natural</span>
    <span class="big l4">results</span>
  </div>

  <header class="title">
    <h1>Micro-needling</h1>
    <h2>PACKAGES</h2>
  </header>

  <p class="intro">Thank you for visiting Morvela Cosmetic Clinic. We offer a range of attractive packages to make your skin journey even more enjoyable.</p>
  <p class="benefit">Microneedling improves your skin’s radiance, lifts your skin and helps fade dark spots and blemishes.</p>

  <div class="package package-3">
    <div class="label">3 microneedling<br>sessions</div>
    <div class="price"><span class="amount">$750</span><span class="save">SAVE 30%</span></div>
  </div>
  <div class="package package-6">
    <div class="label">6 microneedling<br>sessions</div>
    <div class="price"><span class="amount">$1400</span><span class="save">SAVE 35%</span></div>
  </div>

  <div class="facial-banner">Radiance or PRP Plasma Facial</div>

  <div class="facial facial-1">
    <p class="desc">Series of 3 Facials<br>with 1 vial</p>
    <div class="tag"><span class="amount">$1147</span><span class="save">SAVE 15%</span></div>
  </div>
  <div class="facial facial-2">
    <p class="desc">Series of 3 Facials<br>with 2 vials</p>
    <div class="tag"><span class="amount">$2160</span><span class="save">SAVE 20%</span></div>
  </div>
  <div class="facial facial-3">
    <p class="desc">Series of 3 Facials<br>with 3 vials</p>
    <div class="tag"><span class="amount">$3037</span><span class="save">SAVE 25%</span></div>
  </div>
  <div class="facial facial-4">
    <p class="desc">Series of 3 Facials<br>with 4 vial</p>
    <div class="tag"><span class="amount">$3780</span><span class="save">SAVE 30%</span></div>
  </div>

  <p class="terms">*Terms and Conditions apply</p>

  <footer class="contacts">
    <span class="contact">
      <svg viewBox="0 0 20 20" fill="none" stroke="#fff" stroke-width="1.5"><circle cx="10" cy="10" r="8.5"/><path d="M7,6 L8.5,6 L9.3,8 L8.3,8.9 C8.8,10 9.8,11 11,11.7 L11.9,10.7 L13.9,11.5 L13.9,13 C10,13.3 6.7,10 7,6 Z" fill="#fff" stroke="none"/></svg>
      0800 555 014
    </span>
    <span class="divider"></span>
    <span class="contact">
      <svg viewBox="0 0 20 20" fill="none" stroke="#fff" stroke-width="1.4"><rect x="2" y="5" width="16" height="11"/><path d="M2,5 L10,11 L18,5"/></svg>
      ilse@morvela.co.nz
    </span>
    <span class="divider"></span>
    <span class="contact">
      <svg viewBox="0 0 20 20" fill="none" stroke="#fff" stroke-width="1.3"><circle cx="10" cy="10" r="8"/><ellipse cx="10" cy="10" rx="3.5" ry="8"/><path d="M2,10 H18 M3.5,6 H16.5 M3.5,14 H16.5"/></svg>
      www.morvela.co.nz
    </span>
  </footer>
</main>
</body>
</html>
```